Label for Gin Bottle - Cranberry & Peach

Hi, We have created a Cranberry & Peach Gin that we require a label for.
The gin will be a vivid Orange/red colour in a clear 50cl bottle
The gin will be 40% Vol.
I am looking for a classy design with a summer/fresh appearance.
Thank You.

```html
<!DOCTYPE html>
<html lang="en">
<head>
<meta charset="UTF-8">
<title>Cranberry and Peach Gin – Label</title>
<link rel="stylesheet" href="https://fonts.googleapis.com/css2?family=Montserrat:wght@500&family=Playfair+Display:wght@400&display=swap">
<style>
  :root {
    --paper: #ffffff;
    --panel: #f8f7f7;
    --cranberry: #9b1622;
    --plum: #6a2f5f;
    --peach: #f2a482;
    --peach-light: #fbd5c2;
    --blush: #f7b9a0;
  }
  * { margin: 0; padding: 0; box-sizing: border-box; }
  html, body {
    width: 1200px;
    height: 800px;
    overflow: hidden;
    background: var(--paper);
  }
  .gin-label {
    position: relative;
    width: 1200px;
    height: 800px;
    background: var(--paper);
    overflow: hidden;
  }
  .brush-band {
    position: absolute;
    left: 0;
    width: 100%;
  }
  .brush-band--top {
    top: 0;
    height: 83px;
    background: linear-gradient(90deg,
      var(--peach-light) 0%, var(--cranberry) 14%, var(--blush) 30%,
      var(--peach-light) 45%, var(--cranberry) 62%, var(--peach) 78%,
      var(--cranberry) 92%, var(--peach-light) 100%);
    opacity: 0.55;
  }
  .brush-band--bottom {
    bottom: 0;
    height: 122px;
    background: linear-gradient(90deg,
      var(--peach) 0%, var(--peach-light) 12%, var(--cranberry) 26%,
      var(--blush) 40%, var(--peach-light) 54%, var(--cranberry) 70%,
      var(--peach) 84%, var(--cranberry) 100%);
    opacity: 0.6;
  }
  .label-panel {
    position: absolute;
    left: 0;
    top: 83px;
    width: 100%;
    height: 597px;
    background: var(--panel);
  }
  .label-type {
    position: absolute;
    inset: 0;
    width: 1200px;
    height: 800px;
  }
  .flavour {
    font-family: "Montserrat", Arial, sans-serif;
    font-weight: 500;
    font-size: 37px;
    fill: var(--cranberry);
  }
  .spirit {
    font-family: "Playfair Display", Georgia, serif;
    font-weight: 400;
    font-size: 450px;
    fill: var(--plum);
  }
  .strength {
    font-family: "Montserrat", Arial, sans-serif;
    font-weight: 500;
    font-size: 23px;
    fill: var(--peach);
  }
</style>
</head>
<body>
  <main class="gin-label">
    <div class="brush-band brush-band--top" role="img" aria-label="Loose painted brush strokes in cranberry red and peach tones"></div>
    <div class="brush-band brush-band--bottom" role="img" aria-label="Loose painted brush strokes in cranberry red and peach tones"></div>
    <div class="label-panel"></div>
    <svg class="label-type" viewBox="0 0 1200 800" xmlns="http://www.w3.org/2000/svg">
      <text class="flavour" x="600" y="183" text-anchor="middle" textLength="643" lengthAdjust="spacing">CRANBERRY AND PEACH</text>
      <text class="spirit" x="600" y="530" text-anchor="middle" textLength="417" lengthAdjust="spacingAndGlyphs">GIN</text>
      <text class="strength" x="600" y="630" text-anchor="middle" textLength="317" lengthAdjust="spacing">40% VOL ALCOHOL</text>
    </svg>
  </main>
</body>
</html>
```